Brisbane IT support business needs our first website

Hi All,

We are after a new website design for our IT solutions and support business.The business name is Kestrel Harbour Computing Services, or KHCS for short. We provide a range of solutions and services within the IT space.

I would like to utilize the two colours in our business logo I have uploaded.

I understand this is initially for the design only aspect of the site, but I would like to engage the winner to finish coding the website and finalize after also.

Target Market(s)

Other businesses owners and home users.

Industry/Entity Type

Business

Requirements
Must have
• Nice clean and functional design utilizing our business colours from the logo.

```html
<!DOCTYPE html>
<html lang="en">
<head>
<meta charset="utf-8">
<title>Kestrel Harbour Computing Services</title>
<link rel="stylesheet" href="https://fonts.googleapis.com/css2?family=Figtree:wght@500;600;700&family=Lato:ital,wght@0,300;0,400;0,700;0,900;1,400;1,700&display=swap">
<style>
:root{
  --navy:#0b4a66;
  --navy-deep:#083a52;
  --orange:#f08024;
  --ink:#333;
  --muted:#666;
  --rule:#c9c9c9;
  --quote-bg:#f1f1f1;
  --foot:#222;
  --foot-mid:#333;
  --foot-base:#111;
  --white:#fff;
}
*{margin:0;padding:0;box-sizing:border-box}
html,body{width:1200px;height:1108px;overflow:hidden;background:var(--white)}
body{position:relative;font-family:"Lato",sans-serif;color:var(--ink)}
.abs{position:absolute}

/* header */
.brand{left:131px;top:12px;display:flex;align-items:center;gap:14px;height:94px}
.brand-mark{width:94px;height:94px;border-radius:50%;background:var(--navy)}
.brand-name{font-family:"Figtree",sans-serif;font-weight:700;font-size:44px;color:var(--orange);letter-spacing:1px}
.contact-top{top:18px;right:131px;display:flex;align-items:center;gap:18px;font-family:"Figtree",sans-serif;color:var(--navy)}
.contact-top .item{display:flex;align-items:center;gap:10px}
.contact-top .email{font-size:14.5px;font-weight:600}
.contact-top .phone{font-size:20px;font-weight:600}
.nav{top:80px;right:131px;display:flex;align-items:center;font-family:"Figtree",sans-serif;font-weight:600;font-size:14px;color:var(--ink)}
.nav a{color:inherit;text-decoration:none;padding:0 15px;border-left:1px solid #ccc;line-height:12px;position:relative}
.nav a:first-child{border-left:none}
.nav a:last-child{padding-right:0}
.nav a.active{color:var(--orange)}
.nav a.active::after{content:"";position:absolute;left:17px;right:15px;bottom:-10px;height:3px;background:var(--orange)}

/* hero */
.hero{left:0;top:123px;width:1200px;height:515px;background:linear-gradient(180deg,#0d4663 0%,#2a6580 45%,#2c6478 70%,#1c4d5e 100%)}
.hero-title{top:185px;width:1200px;text-align:center;color:var(--white)}
.hero-title .l1{font-size:58px;line-height:64px;font-weight:300}
.hero-title .l1 b{color:var(--orange);font-weight:900}
.hero-title .l1 span{color:var(--orange)}
.hero-title .l2{font-size:48px;line-height:56px;font-weight:300}
.hero-rule{left:461px;top:322px;width:278px;height:1px;background:rgba(255,255,255,.45)}
.card{top:397px;width:169px;height:178px;background:rgba(40,120,150,.55);border-radius:3px;text-align:center;color:var(--white);font-family:"Figtree",sans-serif;font-weight:600;font-size:20px;line-height:26px}
.card .disc{width:80px;height:80px;border-radius:50%;background:var(--orange);margin:17px auto 14px;display:flex;align-items:center;justify-content:center}
.arrow{top:464px}

/* reviews */
.section-title{top:675px;width:1200px;text-align:center;font-family:"Figtree",sans-serif;font-weight:600;font-size:29px;color:var(--navy)}
.section-sub{top:712px;width:1200px;text-align:center;font-size:15.5px;color:var(--muted)}
.divider{top:740px;left:356px}
.quote{left:131px;top:775px;width:830px;height:99px}
.quote-text{left:149px;top:787px;width:750px;font-style:italic;font-size:14px;line-height:24px;color:#444}
.quote-text .mark{display:inline-block;width:22px;height:18px;vertical-align:-3px;margin-right:6px}
.avatar{left:931px;top:767px;width:120px;height:120px;border-radius:50%;border:4px solid #e6e6e6;background:linear-gradient(160deg,#cfe2ee 0%,#8fb3c8 55%,#5f86a0 100%)}
.reviewer{top:892px;right:265px;font-weight:700;font-style:italic;font-size:13px;color:var(--ink)}

/* footer */
.footer{left:0;top:940px;width:1200px;height:103px;background:var(--foot)}
.footer-mid{left:502px;top:940px;width:196px;height:103px;background:var(--foot-mid)}
.foot-heading{font-size:15.5px;line-height:20px;font-weight:700;color:var(--white)}
.news-input{left:197px;top:988px;width:170px;height:26px;background:var(--white);font-style:italic;font-size:11px;color:#555;padding:7px 12px}
.news-btn{left:367px;top:988px;width:91px;height:26px;background:var(--orange);color:var(--white);font-family:"Figtree",sans-serif;font-weight:600;font-size:13.5px;text-align:center;line-height:26px}
.social{top:987px;width:29px;height:29px;border-radius:50%;background:var(--white)}
.foot-text{color:var(--white);font-size:13.5px;line-height:18.5px}
.foot-text.bold{font-weight:700}
.copyright{left:0;top:1043px;width:1200px;height:65px;background:var(--foot-base);color:var(--white);font-size:13.5px;text-align:center;line-height:62px}
</style>
</head>
<body>

<header>
  <div class="abs brand">
    <div class="brand-mark"></div>
    <div class="brand-name">KHCS</div>
  </div>

  <div class="abs contact-top">
    <div class="item">
      <svg width="36" height="34" viewBox="0 0 36 34"><path d="M3 2h24v10l6 5-6 5v10H3z" fill="none" stroke="#f08024" stroke-width="2"/><rect x="9" y="12" width="13" height="9" fill="#f08024"/><path d="M9 12l6.5 5 6.5-5" fill="none" stroke="#fff" stroke-width="1.3"/></svg>
      <span class="email">Info@youremail.com</span>
    </div>
    <div class="item">
      <svg width="36" height="34" viewBox="0 0 36 34"><path d="M3 2h24v10l6 5-6 5v10H3z" fill="none" stroke="#f08024" stroke-width="2"/><rect x="11" y="9" width="9" height="16" rx="1.5" fill="#f08024"/><rect x="13" y="11" width="5" height="7" fill="#fff"/></svg>
      <span class="phone">123-456-7890</span>
    </div>
  </div>

  <nav class="abs nav">
    <a class="active">HOME</a><a>ABOUT</a><a>SERVICES</a><a>TECHNOLOGY</a><a>SOLUTIONS</a><a>SUPPORT</a><a>CONTACT</a>
  </nav>
</header>

<section>
  <div class="abs hero" role="img" aria-label="City skyline and river bridge photograph under a navy tint"></div>
  <div class="abs hero-title">
    <div class="l1"><b>Success</b> <span>With</span></div>
    <div class="l2">Our Creative Solutions</div>
  </div>
  <div class="abs hero-rule"></div>

  <svg class="abs arrow" style="left:131px" width="26" height="46" viewBox="0 0 26 46"><path d="M24 1L2 23l22 22" fill="none" stroke="rgba(255,255,255,.6)" stroke-width="2"/></svg>
  <svg class="abs arrow" style="left:1044px" width="26" height="46" viewBox="0 0 26 46"><path d="M2 1l22 22L2 45" fill="none" stroke="rgba(255,255,255,.6)" stroke-width="2"/></svg>

  <div class="abs card" style="left:188px">
    <div class="disc"><svg width="46" height="46" viewBox="0 0 46 46"><path d="M34 4a9 9 0 0 0-9 12L8 33a4 4 0 0 0 5 5l17-17a9 9 0 0 0 12-9l-6 5-6-2-2-6z" fill="#fff"/></svg></div>
    IT<br>Support
  </div>
  <div class="abs card" style="left:403px">
    <div class="disc"><svg width="44" height="50" viewBox="0 0 44 50"><ellipse cx="22" cy="8" rx="20" ry="7" fill="#fff"/><path d="M2 12c0 5 40 5 40 0v9c0 5-40 5-40 0zM2 25c0 5 40 5 40 0v9c0 5-40 5-40 0zM2 38c0 5 40 5 40 0v4c0 9-40 9-40 0z" fill="#fff"/></svg></div>
    Data<br>Management
  </div>
  <div class="abs card" style="left:628px">
    <div class="disc"><svg width="52" height="40" viewBox="0 0 52 40"><path d="M2 8l10-4 14 8 14-8 10 4v14l-8 3-14 12-6-4-16-10z" fill="#fff"/><path d="M20 16l8 6M18 22l8 6M16 28l6 5" stroke="#f08024" stroke-width="2"/></svg></div>
    Customer<br>Relationship
  </div>
  <div class="abs card" style="left:844px">
    <div class="disc"><svg width="36" height="44" viewBox="0 0 36 44"><path d="M8 20v-7a10 10 0 0 1 20 0v7" fill="none" stroke="#fff" stroke-width="5"/><rect x="2" y="19" width="32" height="24" rx="3" fill="#fff"/></svg></div>
    100%<br>Secure
  </div>
</section>

<section>
  <h2 class="abs section-title">Our Customer Review</h2>
  <p class="abs section-sub">Lorem ipsum dolor sit amet, consectetur Donec a consequat mag&nbsp; Aenean eu velit&nbsp; Aenean sollicitudin</p>
  <svg class="abs divider" width="488" height="18" viewBox="0 0 488 18"><line x1="0" y1="9" x2="214" y2="9" stroke="#c9c9c9"/><line x1="274" y1="9" x2="488" y2="9" stroke="#c9c9c9"/><g fill="#c4c4c4"><path d="M226 2l2 5h5l-4 3 1.5 5-4.5-3-4.5 3 1.5-5-4-3h5z"/><path d="M244 2l2 5h5l-4 3 1.5 5-4.5-3-4.5 3 1.5-5-4-3h5z"/><path d="M261 2l2 5h5l-4 3 1.5 5-4.5-3-4.5 3 1.5-5-4-3h5z"/></g></svg>

  <svg class="abs quote" width="830" height="112" viewBox="0 0 830 112" style="height:112px"><path d="M0 4a4 4 0 0 1 4-4h768l36 32v67H716l-12 12-12-12H4a4 4 0 0 1-4-4z" fill="#f1f1f1"/></svg>
  <p class="abs quote-text"><svg class="mark" viewBox="0 0 22 18"><path d="M2 18V9c0-5 3-8 7-9v3c-2 1-3 3-3 5h3v10zM13 18V9c0-5 3-8 7-9v3c-2 1-3 3-3 5h3v10z" fill="#bdbdbd"/></svg>Lorem sum dolor sit amet, consectetuer adipiscing elit, sed diam nonummy nibh euismod tincidunt ut laoreet re agn aliqam erat volutpat wisi enim ad minim veniam, quis nostrud exerci tation ullamcorper suscipit lobortis nisl ut aliquip modo conseuatis autem vel eum iriure dolor in hendrerit in vulputate velit esse molestie consequat, vel illum dolore eu.</p>
  <div class="abs avatar" role="img" aria-label="Portrait photograph of the reviewer"></div>
  <p class="abs reviewer">Daniel, Harlow Digital , USA</p>
</section>

<footer>
  <div class="abs footer"></div>
  <div class="abs footer-mid"></div>

  <svg class="abs" style="left:131px;top:964px" width="50" height="48" viewBox="0 0 50 48"><path d="M2 18L25 2l23 16v28H2z" fill="none" stroke="#fff" stroke-width="2.5"/><rect x="10" y="6" width="28" height="22" fill="#fff"/><path d="M2 18l23 16 23-16M2 46l18-14M48 46L30 32" fill="none" stroke="#fff" stroke-width="2.5"/><path d="M10 22l15 10 15-10" fill="none" stroke="#222" stroke-width="2"/></svg>
  <h4 class="abs foot-heading" style="left:199px;top:958px">Sign up for Newsletter</h4>
  <div class="abs news-input">Your Email Address</div>
  <div class="abs news-btn">SUBSCRIBE</div>

  <h4 class="abs foot-heading" style="left:530px;top:958px">Follow us on</h4>
  <div class="abs social" style="left:530px"></div>
  <div class="abs social" style="left:568px"></div>
  <div class="abs social" style="left:607px"></div>
  <div class="abs social" style="left:645px"></div>

  <svg class="abs" style="left:734px;top:962px" width="12" height="16" viewBox="0 0 12 16"><path d="M6 0a6 6 0 0 1 6 6c0 4-6 10-6 10S0 10 0 6a6 6 0 0 1 6-6z" fill="#fff"/><circle cx="6" cy="6" r="2.2" fill="#222"/></svg>
  <p class="abs foot-text" style="left:756px;top:959px">123&nbsp; Lorem Sum Dolor<br>Sit Amet Consectuer<br>Adipiscing Elit</p>

  <svg class="abs" style="left:918px;top:962px" width="10" height="16" viewBox="0 0 10 16"><rect x="0.5" y="0.5" width="9" height="15" rx="1.5" fill="none" stroke="#fff"/><rect x="2" y="3" width="6" height="8" fill="#fff"/></svg>
  <p class="abs foot-text bold" style="left:948px;top:959px">(123) 456-7890</p>
  <svg class="abs" style="left:915px;top:999px" width="15" height="11" viewBox="0 0 15 11"><rect width="15" height="11" fill="#fff"/><path d="M0 0l7.5 6L15 0" fill="none" stroke="#222" stroke-width="1.3"/></svg>
  <p class="abs foot-text" style="left:948px;top:995px">info@kestrelharbour.com</p>

  <div class="abs copyright">© 2014 Kestrel Harbour Computing Services. All Rights Reserved.</div>
</footer>

</body>
</html>
```